Coralbend Pastoral Traders Business Cards

We require business cards revamped with our logo. A few details we would like to use.

1. Round Edges
2. Our logo over the top of a wagyu cattle background photo on one side of the card

Other side of the card has the below details.

1. Person Name (First & Last)
2. Job Position
3. Mobile Number
4. Email Address
5. Website Address

Simple & Neat.

Target Market(s)

Sales

Industry/Entity Type

Agriculture

Contact Information for Business Card

CORALBEND PASTORAL TRADERS

Colors

Designer to choose colors to be used in the design.

Requirements
Must have
• Company Logo

```html
<!DOCTYPE html>
<html lang="en">
<head>
<meta charset="utf-8">
<title>Coralbend Pastoral Traders – Business Cards</title>
<link rel="stylesheet" href="https://fonts.googleapis.com/css2?family=Lato:wght@400;700&family=Montserrat:wght@500;800&display=swap">
<style>
  :root {
    --stage: #2b2c2e;
    --wine: #5e0f25;
    --paper: #ffffff;
    --ink-soft: #6b6b6b;
    --ink: #333333;
  }
  * { box-sizing: border-box; margin: 0; padding: 0; }
  html, body { width: 1200px; height: 952px; overflow: hidden; }
  body {
    background: var(--stage);
    font-family: "Lato", Arial, sans-serif;
    display: flex;
    align-items: center;
    justify-content: center;
    gap: 40px;
  }
  .card {
    width: 525px;
    height: 300px;
    border-radius: 14px;
    position: relative;
    overflow: hidden;
    box-shadow: 0 14px 30px rgba(0,0,0,.45);
  }
  /* Contact side */
  .card--contact { background: var(--paper); }
  .contact-band {
    position: absolute;
    left: 0; top: 152px;
    width: 340px; height: 112px;
    background: var(--wine);
    overflow: hidden;
  }
  .contact-band::after {
    content: "";
    position: absolute;
    left: 250px; top: 60px;
    width: 240px; height: 240px;
    border-radius: 50%;
    background: var(--paper);
  }
  .person {
    position: absolute;
    left: 150px; top: 48px;
  }
  .person__name {
    font-family: "Montserrat", Arial, sans-serif;
    font-weight: 500;
    font-size: 22px;
    color: var(--wine);
    letter-spacing: .3px;
  }
  .person__name strong { font-weight: 800; }
  .person__role {
    font-size: 15px;
    color: var(--ink-soft);
    margin-top: 2px;
  }
  .address {
    position: absolute;
    left: 150px; top: 118px;
    display: flex; gap: 8px;
    font-size: 12px; line-height: 1.35;
    color: var(--ink);
  }
  .contact-list {
    position: absolute;
    left: 28px; top: 172px;
    list-style: none;
    z-index: 1;
  }
  .contact-list li {
    display: flex; align-items: center; gap: 9px;
    color: var(--paper);
    font-size: 12.5px;
    margin-bottom: 9px;
    white-space: nowrap;
  }
  .icon { width: 16px; height: 16px; flex: none; }
  /* Brand side */
  .card--brand {
    background: var(--wine);
    display: flex; align-items: center; justify-content: center; gap: 14px;
  }
  .brand-dot {
    width: 34px; height: 34px; border-radius: 50%;
    background: var(--paper);
  }
  .brand-name {
    font-family: "Lato", Arial, sans-serif;
    font-weight: 700;
    color: var(--paper);
    font-size: 26px;
    line-height: 1.15;
    letter-spacing: 2px;
  }
</style>
</head>
<body>
  <section class="card card--contact" aria-label="Business card, contact side">
    <div class="contact-band"></div>
    <div class="person">
      <p class="person__name">DORIAN M. <strong>HALLOWAY</strong></p>
      <p class="person__role">Managing Director</p>
    </div>
    <div class="address">
      <svg class="icon" viewBox="0 0 16 16" aria-hidden="true"><rect width="16" height="16" rx="3" fill="#5e0f25"/><path d="M8 3.2a3 3 0 0 0-3 3c0 2.2 3 6 3 6s3-3.8 3-6a3 3 0 0 0-3-3z" fill="#fff"/><circle cx="8" cy="6.2" r="1.1" fill="#5e0f25"/></svg>
      <p>712 Saltmarsh Road<br>Bramble Creek, QLD 4871</p>
    </div>
    <ul class="contact-list">
      <li><svg class="icon" viewBox="0 0 16 16" aria-hidden="true"><rect width="16" height="16" rx="3" fill="#fff"/><path d="M5 3.5l2 2-1.2 1.3a6 6 0 0 0 3.4 3.4L10.5 9l2 2-1.3 1.5C7.5 12.5 3.5 8.5 3.5 4.8z" fill="#5e0f25"/></svg>+61 412 583 907</li>
      <li><svg class="icon" viewBox="0 0 16 16" aria-hidden="true"><rect width="16" height="16" rx="3" fill="#fff"/><rect x="3.5" y="5" width="9" height="6.5" fill="none" stroke="#5e0f25" stroke-width="1.2"/><path d="M3.5 5l4.5 3.6L12.5 5" fill="none" stroke="#5e0f25" stroke-width="1.2"/></svg>sales@coralbendpastoral.com</li>
      <li><svg class="icon" viewBox="0 0 16 16" aria-hidden="true"><rect width="16" height="16" rx="3" fill="#fff"/><circle cx="8" cy="8" r="4.5" fill="none" stroke="#5e0f25" stroke-width="1.2"/><path d="M3.5 8h9M8 3.5c-2 2.5-2 6.5 0 9M8 3.5c2 2.5 2 6.5 0 9" fill="none" stroke="#5e0f25" stroke-width="1"/></svg>www.coralbendpastoral.com</li>
    </ul>
  </section>

  <section class="card card--brand" aria-label="Business card, brand side">
    <span class="brand-dot"></span>
    <p class="brand-name">CORALBEND<br>PASTORAL TRADERS</p>
  </section>
</body>
</html>
```